Bright Path Attorneys Billboard Design for Personal Injury Law Firm

Need a billboard design that we can use for different versions. 1400px X 400px jpeg or png
I have attached the logo and the attorney for the billboard. Attorney Marla Benning
Here is a link to our current website brightpathlegalgroup.example

HEADLINE: HIT BY A TRUCK?
SUBHEAD: NO FEE. BIG FIGHT.
877-GRANTLY

HEADLINE: ACCIDENT?
SUBHEAD: NO FEE, UNLESS WE WIN!
877-GRANTLY

HEADLINE: BIG TRUCK. BIG CASE.
SUBHEAD: YOU PAY $0 UPFRONT
877-GRANTLY

Target Market(s)

People in Car Accident

Industry/Entity Type

Personal Injury Attorneys

```html
<!DOCTYPE html>
<html lang="en">
<head>
<meta charset="UTF-8">
<title>Bright Path Attorneys – Truck Accident Billboard</title>
<link href="https://fonts.googleapis.com/css2?family=Anton&family=Orbitron:wght@700;800&display=swap" rel="stylesheet">
<style>
  :root {
    --page-bg: #dfe3e8;
    --board-black: #0b0b0b;
    --headline-white: #ffffff;
    --accent-yellow: #f2b61b;
    --mark-green: #5fcf3a;
    --name-panel: #262626;
    --photo-dark: #141414;
    --photo-mid: #2e2e2e;
    --photo-light: #3c3c3c;
  }
  * { margin: 0; padding: 0; box-sizing: border-box; }
  html, body {
    width: 1200px;
    height: 800px;
    overflow: hidden;
    background: var(--page-bg);
  }
  .billboard {
    position: absolute;
    left: 40px;
    top: 193px;
    width: 1120px;
    height: 414px;
    background: var(--board-black);
    overflow: hidden;
  }
  .truck-photo {
    position: absolute;
    right: 0;
    top: 0;
    width: 345px;
    height: 100%;
    background: linear-gradient(90deg, var(--photo-dark) 0%, var(--photo-mid) 45%, var(--photo-light) 100%);
  }
  .message {
    position: absolute;
    left: 50px;
    top: 28px;
    width: 680px;
    text-align: center;
  }
  .headline {
    font-family: "Anton", "Oswald", sans-serif;
    font-weight: 400;
    color: var(--headline-white);
    font-size: 104px;
    line-height: 1;
    letter-spacing: 0.5px;
    text-transform: uppercase;
  }
  .divider {
    display: block;
    width: 630px;
    height: 6px;
    margin: 12px auto 0;
  }
  .subhead {
    font-family: "Anton", "Oswald", sans-serif;
    font-weight: 400;
    color: var(--accent-yellow);
    font-size: 72px;
    line-height: 1;
    margin-top: 12px;
    text-transform: uppercase;
  }
  .phone {
    font-family: "Orbitron", "Arial Black", sans-serif;
    font-weight: 800;
    color: var(--accent-yellow);
    font-size: 60px;
    line-height: 1;
    margin-top: 20px;
    white-space: nowrap;
  }
  .firm-name {
    position: absolute;
    left: 808px;
    top: 312px;
    width: 300px;
    height: 84px;
    background: var(--name-panel);
    display: flex;
    align-items: center;
    gap: 14px;
    padding: 0 18px;
  }
  .firm-name-mark {
    width: 20px;
    height: 20px;
    background: var(--mark-green);
    flex-shrink: 0;
  }
  .firm-name-text {
    font-family: "Orbitron", "Arial", sans-serif;
    font-weight: 700;
    color: var(--headline-white);
    font-size: 17px;
    line-height: 1.3;
    text-transform: uppercase;
  }
</style>
</head>
<body>
  <section class="billboard">
    <div class="truck-photo" role="img" aria-label="Photo of the front of a black semi-truck with chrome grille and headlight"></div>

    <div class="message">
      <h1 class="headline">Hit by a Truck?</h1>
      <svg class="divider" viewBox="0 0 630 6" preserveAspectRatio="none" aria-hidden="true">
        <polygon points="0,3 315,0 630,3 315,6" fill="var(--accent-yellow)"/>
      </svg>
      <p class="subhead">No Fee. Big Fight.</p>
      <svg class="divider" viewBox="0 0 630 6" preserveAspectRatio="none" aria-hidden="true">
        <polygon points="0,3 315,1 630,3 315,5" fill="var(--accent-yellow)"/>
      </svg>
      <p class="phone">877-GRANTLY</p>
    </div>

    <div class="firm-name">
      <span class="firm-name-mark" aria-hidden="true"></span>
      <span class="firm-name-text">Bright Path Attorneys</span>
    </div>
  </section>
</body>
</html>
```